Real Estate Webpage Design

We have an existing website: brindlewoodhomes.com.au
We focus customised service mainly on Property Management and second-hand property sales.
We are not entirely happy about the current design and layout can stay roughly the same as the back end coding is linked to a CRM system.
We would like to see the design are more reachable to our clients and appearing.
Please check our Website Design Draft for more details.

Industry/Entity Type

Real estate Agency

Number of Pages Required

5+ page

Font styles to use
Sans Serif

Colors

Designer to choose colors to be used in the design.

```html
<!DOCTYPE html>
<html lang="en">
<head>
<meta charset="utf-8">
<title>Brindlewood Homes</title>
<link href="https://fonts.googleapis.com/css2?family=Poppins:ital,wght@0,400;0,500;0,600;0,700;0,800;1,400&family=Parisienne&display=swap" rel="stylesheet">
<style>
:root{
  --gold:#e9bb4f;
  --gold-deep:#c99a2e;
  --navy:#263449;
  --ink:#111;
  --grey:#666;
  --line:#ddd;
  --white:#fff;
}
*{box-sizing:border-box;margin:0;padding:0}
html,body{width:1200px;height:3754px;overflow:hidden}
body{position:relative;background:var(--white);font-family:'Poppins',sans-serif;color:var(--ink)}
.abs{position:absolute}

/* header */
.brand{display:flex;align-items:center;gap:10px}
.brand-dot{width:34px;height:34px;border-radius:50%;background:var(--gold)}
.brand-name{font-weight:700;font-size:28px;color:var(--gold);line-height:1}
.brand-sub{font-size:9px;color:var(--gold);margin-top:2px}
.site-header .brand{left:143px;top:26px}
.main-nav{left:480px;top:41px;display:flex;gap:32px;font-size:12px}
.main-nav a{color:var(--ink);text-decoration:none}
.main-nav a.active{color:var(--gold)}
.btn{display:inline-block;background:var(--navy);color:var(--white);font-size:12px;font-weight:500;padding:8px 24px;clip-path:polygon(8px 0,100% 0,calc(100% - 8px) 100%,0 100%);box-shadow:none;position:relative}
.btn-wrap{position:absolute}
.btn-wrap::after{content:"";position:absolute;right:-6px;top:0;width:4px;height:100%;background:var(--gold);transform:skewX(-18deg)}
.header-cta{left:992px;top:34px}

/* hero */
.hero-photo{left:0;top:98px;width:1200px;height:477px;clip-path:polygon(65px 0,1200px 0,1136px 100%,0 100%);
  background:linear-gradient(90deg,#c8992f 0%,#d7a93c 55%,#e8e3d8 62%,#f4f2ee 78%,#c9a646 92%)}
.hero-strip{left:0;top:131px}
.hero-band{left:0;top:582px;width:1110px;height:25px;background:var(--navy);clip-path:polygon(0 0,100% 0,calc(100% - 4px) 100%,0 100%)}
.hero-copy{left:173px;top:262px;color:var(--white)}
.hero-copy .kicker{font-size:25px;font-weight:400}
.hero-copy h1{font-size:40px;font-weight:700;line-height:1.2;letter-spacing:-.5px}
.hero-copy p{font-size:11.5px;line-height:21px;width:420px;margin-top:10px}
.hero-copy .btn-wrap{left:0;top:150px;position:absolute}

/* about */
.about-frame{left:0;top:762px;width:435px;height:480px;background:var(--gold);clip-path:polygon(0 0,355px 0,435px 100%,0 100%)}
.about-frame-inner{left:0;top:770px;width:420px;height:462px;background:var(--white);clip-path:polygon(0 0,345px 0,420px 100%,0 100%)}
.about-photo{left:0;top:747px;width:412px;height:477px;clip-path:polygon(0 0,345px 0,412px 100%,0 100%);
  background:linear-gradient(160deg,#3a5a8a 0%,#7e98bb 35%,#e6e8ea 55%,#c9cdd2 80%,#6a7078 100%)}
.about-copy{left:497px;top:824px;width:550px}
.about-copy h2{font-size:46px;font-weight:700;line-height:1.2}
.about-copy .tag{font-size:19px;font-weight:600;color:var(--gold)}
.about-copy p{font-size:11px;color:#444;line-height:24px;margin-top:26px}

/* listings */
.listings-gold-r{left:1143px;top:1398px;width:57px;height:820px;background:var(--gold);clip-path:polygon(0 0,22px 0,57px 100%,0 100%)}
.listings-gold-b{left:66px;top:2196px;width:1134px;height:22px;background:var(--gold)}
.listings-panel{left:0;top:1367px;width:1183px;height:820px;background:var(--navy);clip-path:polygon(0 0,1133px 0,100% 100%,0 100%)}
.listings-head{left:0;top:1450px;width:1200px;text-align:center;color:var(--white)}
.listings-head .small{font-size:19px;font-weight:500}
.listings-head h2{font-size:47px;font-weight:700;line-height:1.1}
.listings-head h2 span{color:var(--gold)}
.filters{left:0;top:1552px;width:1200px;display:flex;justify-content:center;gap:48px;font-size:11.5px;color:var(--white)}
.filters .active{color:var(--gold)}
.card{width:216px;height:430px;top:1638px;border:2px solid var(--gold);color:var(--white);padding:14px 14px}
.card.featured{background:linear-gradient(180deg,#e9bb4f,#c89b35)}
.card-photo{width:188px;height:200px;background:linear-gradient(180deg,#e8e3da 0%,#d8cfc0 45%,#9f7a52 75%,#c7b08d 100%)}
.card h3{font-size:19px;font-weight:600;color:var(--gold);margin-top:20px}
.card.featured h3{color:var(--white)}
.card p{font-size:9.5px;line-height:19px;opacity:.85}
.card .strong{font-weight:600;opacity:1}
.card hr{border:0;border-top:1px solid rgba(255,255,255,.7);margin:10px 0 14px}
.card .feats{display:flex;align-items:center;font-size:10px}
.card .feats span{display:flex;align-items:center;gap:4px;padding:0 12px}
.card .feats span:first-child{padding-left:4px}
.card .feats span+span{border-left:1px solid rgba(255,255,255,.8)}

/* testimonials */
.testi{left:0;top:2355px;width:1200px;text-align:center}
.testi h2{font-size:46px;font-weight:700;line-height:1.1}
.testi .tag{font-size:19px;font-weight:500;color:var(--gold)}
.testi blockquote{width:700px;margin:38px auto 0;font-style:italic;font-size:19.5px;line-height:29px;color:#333}
.testi .q{color:var(--gold);font-size:46px;font-weight:700;font-style:normal;line-height:0;vertical-align:-14px}
.testi .sig{font-family:'Parisienne',cursive;font-size:34px;margin-top:36px;color:#333}
.arrow{width:42px;height:42px;border:1.5px solid var(--gold);top:2495px;display:flex;align-items:center;justify-content:center}

/* contact */
.contact-photo{left:0;top:2803px;width:1200px;height:477px;clip-path:polygon(65px 0,1200px 0,1136px 100%,0 100%);
  background:linear-gradient(135deg,#a9822a 0%,#c79c3a 45%,#dcb24e 100%)}
.contact-strip{left:0;top:2836px}
.contact-band{left:0;top:3288px;width:1110px;height:25px;background:var(--navy)}
.contact-copy{left:168px;top:2995px;color:var(--white)}
.contact-copy h2{font-size:46px;font-weight:700}
.contact-copy p{font-size:11.5px;line-height:24px;width:370px;margin-top:14px}
.contact-form{left:590px;top:2871px;width:509px;height:354px;background:var(--white);clip-path:polygon(20px 0,100% 0,calc(100% - 20px) 100%,0 100%);padding:72px 0 0 94px}
.field{width:336px;border-bottom:1px solid #888;font-size:12.5px;color:#444;padding-bottom:4px;margin-bottom:28px}
.field.msg{height:72px}
.contact-form .btn-wrap{left:178px;top:278px}

/* footer */
.site-footer .brand{left:148px;top:3390px}
.footer-about{left:149px;top:3455px;font-size:11.5px;line-height:24px;color:#444;width:260px}
.footer-h{font-size:17px;font-weight:600}
.footer-links{font-size:11.5px;line-height:29px;color:#444;list-style:none}
.footer-links li::before{content:"›";color:var(--gold);margin-right:6px}
.contact-item{display:flex;gap:10px;font-size:11.5px;line-height:24px;color:#444}
.footer-rule{left:98px;top:3611px;width:1004px;height:1px;background:var(--line)}
.copyright{left:0;top:3643px;width:1200px;text-align:center;font-size:11.5px;color:#444}
.socials{left:0;top:3682px;width:1200px;display:flex;justify-content:center;gap:6px}
.socials span{width:25px;height:25px;border-radius:50%;background:var(--gold)}
</style>
</head>
<body>

<header class="site-header">
  <div class="brand abs"><span class="brand-dot"></span><div><div class="brand-name">Brindlewood</div><div class="brand-sub">Homes</div></div></div>
  <nav class="main-nav abs">
    <a class="active" href="#">Home</a><a href="#">About Us</a><a href="#">Leasing</a><a href="#">Buy</a><a href="#">Sell</a><a href="#">Our Team</a><a href="#">Blog</a>
  </nav>
  <div class="btn-wrap header-cta"><span class="btn">Contact Us</span></div>
</header>

<section class="hero">
  <div class="hero-photo abs" role="img" aria-label="Modern white apartment building with stacked balconies under a warm gold tint"></div>
  <svg class="hero-strip abs" width="56" height="444" viewBox="0 0 56 444"><polygon points="40,0 56,0 16,444 0,444" fill="#263449"/></svg>
  <div class="hero-band abs"></div>
  <div class="hero-copy abs">
    <div class="kicker">WELCOME TO</div>
    <h1>PROPERTY SOLUTIONS</h1>
    <p>At Brindlewood, “the home, the house”, buying a property is one of the most expensive expenses and important assets.</p>
    <div class="btn-wrap"><span class="btn">Contact Us</span></div>
  </div>
</section>

<section class="about">
  <div class="about-frame abs"></div>
  <div class="about-frame-inner abs"></div>
  <div class="about-photo abs" role="img" aria-label="White modern house with glass balconies against a blue sky"></div>
  <div class="about-copy abs">
    <h2>Brindlewood</h2>
    <div class="tag">Built around “the home”</div>
    <p>At Brindlewood, “the home, the house”, buying a property is one of the most expensive expenses and important assets for people. Brindlewood is a real estate company located in Ashgrove, Canberra.</p>
    <p>Being a portfolio sales agent and property manager, coupled with our high-profile international real estate experience, Brindlewood is considered a market leader on the cutting edge with deep industry knowledge, ranging from landlord-tenant relationships, residential purchases.</p>
  </div>
</section>

<section class="listings">
  <div class="listings-gold-r abs"></div>
  <div class="listings-gold-b abs"></div>
  <div class="listings-panel abs"></div>
  <div class="listings-head abs"><div class="small">This Month At</div><h2>Brindlewood <span>Homes</span></h2></div>
  <div class="filters abs"><span>For Sale</span><span class="active">For Lease</span><span>Open Times</span><span>Sold</span><span>Leased</span></div>

  <article class="card abs" style="left:124px">
    <div class="card-photo" role="img" aria-label="Bright living room with striped sofa"></div>
    <h3>Lawson</h3><p>14/22 Willow Terrace Lawson</p><p>$640 - $660 pw</p><p class="strong">Next Inspection:</p><p>Sat 21st May 02:30 PM - 02:45 PM</p>
    <hr><div class="feats"><span>3 ⎓</span><span>2 ◡</span><span>2 ⛟</span></div>
  </article>
  <article class="card featured abs" style="left:368px">
    <div class="card-photo" role="img" aria-label="Living room with teal cushions and large windows" style="background:linear-gradient(180deg,#dfe3e4,#b8c0c2 50%,#6b6460 80%,#8a8580)"></div>
    <h3>Red Hill</h3><p>14/22 Willow Terrace Lawson</p><p>$640 - $660 pw</p><p class="strong">Next Inspection:</p><p>Sat 21st May 02:30 PM - 02:45 PM</p>
    <hr><div class="feats"><span>3 ⎓</span><span>2 ◡</span><span>2 ⛟</span></div>
  </article>
  <article class="card abs" style="left:613px">
    <div class="card-photo" role="img" aria-label="Dining room with wooden table and cream chairs" style="background:linear-gradient(180deg,#cdbfa8,#a88862 50%,#e8dcc8 85%)"></div>
    <h3>Braddon</h3><p>14/22 Willow Terrace Lawson</p><p>$640 - $660 pw</p><p class="strong">Next Inspection:</p><p>Sat 21st May 02:30 PM - 02:45 PM</p>
    <hr><div class="feats"><span>3 ⎓</span><span>2 ◡</span><span>2 ⛟</span></div>
  </article>
  <article class="card abs" style="left:859px">
    <div class="card-photo" role="img" aria-label="Bright living room with striped sofa"></div>
    <h3>Griffith</h3><p>14/22 Willow Terrace Lawson</p><p>$640 - $660 pw</p><p class="strong">Next Inspection:</p><p>Sat 21st May 02:30 PM - 02:45 PM</p>
    <hr><div class="feats"><span>3 ⎓</span><span>2 ◡</span><span>2 ⛟</span></div>
  </article>
</section>

<section class="testimonials">
  <div class="testi abs">
    <h2>Testimonials</h2>
    <div class="tag">What others Say</div>
    <blockquote><span class="q">“</span> Megan is my best property manager! Always happy to response my queries and keep us well informed at all stage.&nbsp; I will definitely recommend her to my friends. <span class="q">”</span></blockquote>
    <div class="sig">Tom Hartley</div>
  </div>
  <div class="arrow abs" style="left:158px"><svg width="12" height="16" viewBox="0 0 12 16"><path d="M9 1 2 8l7 7" fill="none" stroke="#333" stroke-width="1.5"/></svg></div>
  <div class="arrow abs" style="left:1005px"><svg width="12" height="16" viewBox="0 0 12 16"><path d="M3 1l7 7-7 7" fill="none" stroke="#333" stroke-width="1.5"/></svg></div>
</section>

<section class="contact">
  <div class="contact-photo abs" role="img" aria-label="Modern house exterior under a warm gold overlay"></div>
  <svg class="contact-strip abs" width="56" height="444" viewBox="0 0 56 444"><polygon points="40,0 56,0 16,444 0,444" fill="#263449"/></svg>
  <div class="contact-band abs"></div>
  <div class="contact-copy abs">
    <h2>Contact Form</h2>
    <p>At Brindlewood, “the home, the house”, buying a property is one of the most expensive expenses and important assets for people.</p>
  </div>
  <form class="contact-form abs">
    <div class="field">Name</div>
    <div class="field">Email</div>
    <div class="field msg">Message</div>
    <div class="btn-wrap"><span class="btn" style="padding:8px 36px">Submit</span></div>
  </form>
</section>

<footer class="site-footer">
  <div class="brand abs"><span class="brand-dot"></span><div><div class="brand-name">Brindlewood</div><div class="brand-sub">Homes</div></div></div>
  <p class="footer-about abs">At Brindlewood, “the home, the house”, buying a property is one of the most expensive expenses</p>
  <div class="abs" style="left:540px;top:3388px"><div class="footer-h">Pages</div></div>
  <ul class="footer-links abs" style="left:541px;top:3428px"><li>Home</li><li>About Us</li><li>Leasing</li><li>Buy</li><li>Sell</li></ul>
  <ul class="footer-links abs" style="left:651px;top:3428px"><li>Our Team</li><li>Blog</li><li>Contact Us</li></ul>
  <div class="abs" style="left:884px;top:3388px"><div class="footer-h">Contact Us</div></div>
  <div class="contact-item abs" style="left:884px;top:3434px">
    <svg width="16" height="18" viewBox="0 0 16 18"><path d="M8 17s6-6 6-10A6 6 0 0 0 2 7c0 4 6 10 6 10z" fill="none" stroke="#e9bb4f" stroke-width="1.2"/><circle cx="8" cy="7" r="2" fill="none" stroke="#e9bb4f" stroke-width="1.2"/></svg>
    <div>18/4 Marlow Crescent,<br>Ashgrove, ACT, 2914</div>
  </div>
  <div class="contact-item abs" style="left:884px;top:3507px">
    <svg width="16" height="18" viewBox="0 0 16 18"><path d="M3 2l3 3-2 2c1 3 3 5 6 6l2-2 3 3-2 2C7 16 1 10 1 4z" fill="none" stroke="#e9bb4f" stroke-width="1.2"/></svg>
    <div>P: 02 6100 0142<br>F: 02 6100 0158</div>
  </div>
  <div class="footer-rule abs"></div>
  <div class="copyright abs">Copyright © 2022 All rights reserved&nbsp; | &nbsp;Privacy Policy</div>
  <div class="socials abs"><span></span><span></span><span></span><span></span><span></span></div>
</footer>

</body>
</html>
```